Business Card for a Jewellery Brand

Business card for an upscale jewellery brand. Attached is the brand logo and icon and color board. I am looking for two card versions: one for the founder and one is generic. The card should be elegant and convey upscale and premium feel. I am open to both square and rectangle card shapes.

Industry/Entity Type

Jewelry

Contact Information for Business Card

Two cards: (1) Sunila Perumbadi (Founder) (2) General
(1) Sunila Perumbadi card should have Name: Sunila Perumbadi, Title: Founder Email id: sunila@quelm.com.au. Phone no: +61412555307
(2) Generic card should have Email id: info@quelm.com.au. Phone no: +61431555962

Requirements
Must have
• Workmark
• ICON
• Phone no
• Email ID
• ABN: 48917205563 (Note: ABN is Business number in Australia)
• Website: www.quelm.com.au
• Instagram: quelm_jewellery
• Facebook: @quelmjewellery
Nice to have
• Tagline

```html
<!DOCTYPE html>
<html lang="en">
<head>
<meta charset="utf-8">
<title>QUELM – Business Cards</title>
<link rel="stylesheet" href="https://fonts.googleapis.com/css2?family=Cormorant+Garamond:wght@500;600&display=swap">
<style>
  :root {
    --ink-dark: #1c1c1c;
    --frame-mauve: #8a5d5a;
    --paper: #e9e8e8;
    --frame-blush: #e8b9b8;
    --rose: #e59b97;
    --rose-dusty: #d49896;
    --rose-panel: #e49794;
    --white: #ffffff;
    --text-grey: #4f4f4f;
    --serif: "Cormorant Garamond", serif;
  }
  * { box-sizing: border-box; margin: 0; padding: 0; }
  html, body { width: 1200px; height: 727px; overflow: hidden; background: var(--paper); }
  .sheet { position: relative; width: 1200px; height: 727px; font-family: var(--serif); }

  .card { position: absolute; overflow: hidden; }
  .front-dark { left: 0; top: 0; width: 599px; height: 365px; background: var(--ink-dark); }
  .front-light { left: 599px; top: 0; width: 601px; height: 365px; background: var(--paper); border-bottom: 2px solid var(--white); }
  .generic-back { left: 0; top: 365px; width: 600px; height: 362px; }
  .founder-face { left: 600px; top: 365px; width: 290px; height: 362px; background: var(--rose-panel); border-left: 1px solid var(--white); }
  .founder-contact { left: 890px; top: 365px; width: 310px; height: 362px; background: var(--paper); }

  .frame { position: absolute; border-style: solid; }
  .front-dark .frame { left: 32px; top: 36px; width: 526px; height: 292px; border-width: 5px; border-color: var(--frame-mauve); }
  .front-light .frame { left: 41px; top: 36px; width: 524px; height: 292px; border-width: 5px; border-color: var(--frame-blush); }

  .brand-lockup { position: absolute; left: 0; right: 0; top: 118px; text-align: center; }
  .brand-dot { display: block; width: 18px; height: 18px; margin: 0 auto 22px; border-radius: 50%; background: var(--rose); }
  .wordmark { font-family: var(--serif); font-weight: 600; font-size: 54px; line-height: 1; letter-spacing: 0.32em; padding-left: 0.32em; color: var(--rose); }

  .pattern-field { position: absolute; inset: 0; background: linear-gradient(135deg, #d7a09e 0%, var(--rose-dusty) 50%, #d29492 100%); }
  .contact-frame { position: absolute; left: 109px; top: 65px; width: 383px; height: 232px; border: 2px solid #f3e6e5; background: var(--rose-dusty); text-align: center; }
  .contact-frame .icon { display: block; margin: 0 auto; }
  .contact-frame .mail-icon { margin-top: 52px; }
  .contact-frame .line { font-size: 17px; letter-spacing: 0.14em; color: var(--text-grey); }
  .contact-frame .email { margin-top: 9px; }
  .contact-frame .talk-icon { margin-top: 17px; }
  .contact-frame .phone { margin-top: 4px; letter-spacing: 0.2em; }

  .founder-face .mark { display: block; width: 14px; height: 14px; margin: 121px auto 0; border-radius: 50%; background: var(--white); }
  .person { margin-top: 17px; text-align: center; color: var(--white); font-weight: 500; font-size: 19px; line-height: 24px; letter-spacing: 0.26em; text-transform: uppercase; padding-left: 0.26em; }
  .rule { position: relative; width: 44px; height: 1px; margin: 8px auto 0; background: rgba(255,255,255,0.8); }
  .rule::after { content: ""; position: absolute; left: 21px; top: -2px; width: 1px; height: 5px; background: rgba(255,255,255,0.8); }
  .role { margin-top: 5px; text-align: center; color: var(--white); font-size: 13px; letter-spacing: 0.02em; }

  .contact-row { position: absolute; left: 42px; display: flex; align-items: center; gap: 10px; font-size: 16px; letter-spacing: 0.14em; color: var(--text-grey); }
  .contact-row.email { top: 137px; }
  .contact-row.phone { top: 191px; letter-spacing: 0.2em; }
</style>
</head>
<body>
<main class="sheet">

  <section class="card front-dark">
    <div class="frame"></div>
    <div class="brand-lockup">
      <span class="brand-dot"></span>
      <div class="wordmark">QUELM</div>
    </div>
  </section>

  <section class="card front-light">
    <div class="frame"></div>
    <div class="brand-lockup">
      <span class="brand-dot"></span>
      <div class="wordmark">QUELM</div>
    </div>
  </section>

  <section class="card generic-back">
    <div class="pattern-field" role="img" aria-label="Repeating pattern of the brand icon in soft rose tones"></div>
    <div class="contact-frame">
      <svg class="icon mail-icon" width="27" height="20" viewBox="0 0 27 20" aria-hidden="true">
        <rect x="1" y="1" width="25" height="18" fill="none" stroke="#ffffff" stroke-width="1.6"/>
        <path d="M1 1 L13.5 11 L26 1 M1 19 L10 9 M26 19 L17 9" fill="none" stroke="#ffffff" stroke-width="1.4"/>
      </svg>
      <div class="line email">info@quelm.com.au</div>
      <svg class="icon talk-icon" width="28" height="24" viewBox="0 0 28 24" aria-hidden="true">
        <ellipse cx="14" cy="9" rx="12.5" ry="7.5" fill="none" stroke="#ffffff" stroke-width="2"/>
        <path d="M10 15.5 L9 22 L15 16.5" fill="none" stroke="#ffffff" stroke-width="2" stroke-linejoin="round"/>
      </svg>
      <div class="line phone">+61431555962</div>
    </div>
  </section>

  <section class="card founder-face">
    <span class="mark"></span>
    <div class="person">Sunila<br>Perumbadi</div>
    <div class="rule"></div>
    <div class="role">FOUNDER</div>
  </section>

  <section class="card founder-contact">
    <div class="contact-row email">
      <svg width="27" height="20" viewBox="0 0 27 20" aria-hidden="true">
        <rect x="1" y="1" width="25" height="18" fill="none" stroke="#e59b97" stroke-width="1.8"/>
        <path d="M1 1 L13.5 11 L26 1 M1 19 L10 9 M26 19 L17 9" fill="none" stroke="#e59b97" stroke-width="1.5"/>
      </svg>
      <span>sunila@quelm.com.au</span>
    </div>
    <div class="contact-row phone">
      <svg width="28" height="24" viewBox="0 0 28 24" aria-hidden="true">
        <ellipse cx="14" cy="9" rx="12.5" ry="7.5" fill="none" stroke="#e59b97" stroke-width="2"/>
        <path d="M10 15.5 L9 22 L15 16.5" fill="none" stroke="#e59b97" stroke-width="2" stroke-linejoin="round"/>
      </svg>
      <span>+61412555307</span>
    </div>
  </section>

</main>
</body>
</html>
```